Logo & Visitenkarte für Gesundheit
Zielgruppe
Gesundheitsprodukte
Ernährungsberatung
Aufgabenstellung
nicht spezifisch Logo mit Essen und Trinken. Eher ein allgemeines Logo für Gesundheit

```html
<!DOCTYPE html>
<html lang="de">
<head>
<meta charset="utf-8">
<title>Vita for every day – Visitenkarten</title>
<link href="https://fonts.googleapis.com/css2?family=Roboto:wght@400;700&display=swap" rel="stylesheet">
<style>
  :root {
    --bg: #e6e7e9;
    --teal-dark: #124a59;
    --teal-mid: #256f77;
    --lime: #b5c31a;
    --white: #ffffff;
  }
  * { margin: 0; padding: 0; box-sizing: border-box; }
  html, body { width: 1200px; height: 754px; overflow: hidden; }
  body {
    background: var(--bg);
    font-family: "Roboto", Arial, sans-serif;
    position: relative;
  }
  .card {
    position: absolute;
    width: 414px;
    height: 268px;
  }
  .card--front { background: var(--teal-dark); top: 61px; }
  .card--back { background: var(--white); top: 415px; }
  .pos-left-front { left: 104px; }
  .pos-right-front { left: 681px; }
  .pos-left-back { left: 104px; }
  .pos-right-back { left: 683px; }

  .front-mark {
    position: absolute;
    left: 0; right: 0; top: 86px;
    display: flex; align-items: center; justify-content: center; gap: 10px;
    color: var(--teal-mid);
    font-weight: 700;
    font-size: 26px;
    letter-spacing: 1px;
    text-transform: uppercase;
  }
  .front-mark__dot {
    width: 22px; height: 22px; border-radius: 50%;
    background: var(--lime);
  }
  .front-url {
    position: absolute;
    left: 0; right: 0; top: 240px;
    text-align: center;
    color: var(--white);
    font-size: 10.5px;
  }

  .brand {
    position: absolute;
    right: 22px; top: 26px;
    display: flex; align-items: center; gap: 8px;
    color: var(--lime);
    font-weight: 700;
    font-size: 20px;
    line-height: 1;
    text-transform: uppercase;
    letter-spacing: 0.5px;
  }
  .brand__dot {
    width: 14px; height: 14px; border-radius: 50%;
    background: var(--teal-dark);
  }
  .person {
    position: absolute;
    left: 21px; top: 129px;
    color: var(--teal-dark);
  }
  .person__name { font-weight: 700; font-size: 18.5px; line-height: 1; }
  .person__role { font-size: 14px; line-height: 1; margin-top: 3px; }

  .contact-band {
    position: absolute;
    left: 0; right: 0; top: 170px; height: 75px;
    background: var(--teal-dark);
    color: var(--white);
    font-size: 12.5px;
  }
  .address {
    position: absolute; left: 21px; top: 16px; line-height: 17px;
  }
  .contact-list {
    position: absolute; left: 202px; top: 8px;
    list-style: none;
  }
  .contact-list li {
    display: flex; align-items: center; gap: 10px;
    height: 20px;
  }
  .contact-list svg { width: 16px; height: 16px; flex: none; }
</style>
</head>
<body>

  <section class="card card--front pos-left-front">
    <div class="front-mark"><span class="front-mark__dot"></span>Vita for every day</div>
    <p class="front-url">www.vitaforeveryday.de</p>
  </section>

  <section class="card card--front pos-right-front">
    <div class="front-mark"><span class="front-mark__dot"></span>Vita 4 every day</div>
    <p class="front-url">www.vitaforeveryday.de</p>
  </section>

  <section class="card card--back pos-left-back">
    <div class="brand"><span class="brand__dot"></span>Vita for every day</div>
    <div class="person">
      <p class="person__name">MAX MUSTERMAN</p>
      <p class="person__role">Function</p>
    </div>
    <div class="contact-band">
      <p class="address">Streetnumber 00<br>City name</p>
      <ul class="contact-list">
        <li><svg viewBox="0 0 16 16"><path d="M9 1 L11 2 L8 6 L6 5 C5 8 6 11 8 13 L10 11 L12 13 L10 15 C4 13 2 6 9 1 Z" fill="#fff"/></svg>000000000000</li>
        <li><svg viewBox="0 0 16 16"><rect x="1" y="3" width="14" height="10" fill="none" stroke="#fff" stroke-width="1.5"/><path d="M1 3 L8 9 L15 3 M1 13 L6 8 M15 13 L10 8" fill="none" stroke="#fff" stroke-width="1.5"/></svg>info@vitalebenmehr.de</li>
        <li><svg viewBox="0 0 16 16" fill="none" stroke="#fff" stroke-width="1.2"><circle cx="8" cy="8" r="7"/><ellipse cx="8" cy="8" rx="3" ry="7"/><path d="M1 8 H15 M2 4.5 H14 M2 11.5 H14"/></svg>www.vitalebenmehr.de</li>
      </ul>
    </div>
  </section>

  <section class="card card--back pos-right-back">
    <div class="brand"><span class="brand__dot"></span>Vita 4 every day</div>
    <div class="person">
      <p class="person__name">MAX MUSTERMAN</p>
      <p class="person__role">Function</p>
    </div>
    <div class="contact-band">
      <p class="address">Streetnumber 00<br>City name</p>
      <ul class="contact-list">
        <li><svg viewBox="0 0 16 16"><path d="M9 1 L11 2 L8 6 L6 5 C5 8 6 11 8 13 L10 11 L12 13 L10 15 C4 13 2 6 9 1 Z" fill="#fff"/></svg>000000000000</li>
        <li><svg viewBox="0 0 16 16"><rect x="1" y="3" width="14" height="10" fill="none" stroke="#fff" stroke-width="1.5"/><path d="M1 3 L8 9 L15 3 M1 13 L6 8 M15 13 L10 8" fill="none" stroke="#fff" stroke-width="1.5"/></svg>info@vitalebenmehr.de</li>
        <li><svg viewBox="0 0 16 16" fill="none" stroke="#fff" stroke-width="1.2"><circle cx="8" cy="8" r="7"/><ellipse cx="8" cy="8" rx="3" ry="7"/><path d="M1 8 H15 M2 4.5 H14 M2 11.5 H14"/></svg>www.vitalebenmehr.de</li>
      </ul>
    </div>
  </section>

</body>
</html>
```